Business card

I have changed logo's and colors. I have uploaded the new logo and colors.

In my head I am thinking about the main logo and text beside logo to be on one side of the card. The other side of the card to have just my picture and contact information.

The "R" emblem and the "equal housing" emblem... cut he MLS from the "R". and remove the wording from the house emblem.

Info on Card:

Lyle Penwarden
Designated Broker, CDPE, CNE, GRI
Direct: 602.555.0147
Fax: 623.555.0182
Lyle@PenwardenandPartners.example
www.PenwardenandPartners.example
4915 West Quillmoor Lane Glendale, AZ 85391

Please see brief as I have uploaded a new logo and a few notes.

Reason: I changed the logo and colors. Please see brief

I am leaning towards maybe a black business card(or at least on the front where the logo is). I liked several designs that were submitted. Please re-submit.

```html
<!DOCTYPE html>
<html lang="en">
<head>
<meta charset="utf-8">
<title>Penwarden &amp; Partners — Business Card</title>
<link rel="stylesheet" href="https://fonts.googleapis.com/css2?family=Montserrat:wght@400;500;600&family=Pinyon+Script&display=swap">
<style>
  :root {
    --page-bg: #1b1b1d;
    --card-bg: #1a1718;
    --card-edge: #2a2627;
    --panel-light: #4a4a4c;
    --panel-dark: #2b2b2d;
    --ink-light: #ffffff;
    --ink-soft: #e6e6e6;
    --ink-muted: #d4d4d6;
    --photo-light: #f4f4f4;
    --photo-mid: #b9bcc0;
    --photo-dark: #3a3d44;
  }
  * { margin: 0; padding: 0; box-sizing: border-box; }
  html, body {
    width: 1200px;
    height: 871px;
    overflow: hidden;
    background: var(--page-bg);
  }
  .card {
    position: absolute;
    left: 250px;
    width: 1050px;
    height: 600px;
    overflow: hidden;
    transform: scale(0.6667);
    transform-origin: 0 0;
  }
  .card-front {
    top: 446px;
    background: radial-gradient(ellipse at 30% 40%, var(--card-edge), var(--card-bg) 70%);
  }
  .card-back {
    top: 25px;
    background: linear-gradient(90deg, var(--panel-light) 0%, var(--panel-dark) 55%, var(--card-bg) 56%, var(--card-bg) 100%);
  }
  .card-art {
    position: absolute;
    inset: 0;
  }
  .brand {
    position: absolute;
    display: flex;
    align-items: center;
    gap: 14px;
  }
  .card-front .brand { left: 70px; top: 58px; }
  .card-back .brand { left: 110px; top: 80px; }
  .brand-mark {
    width: 48px;
    height: 48px;
    border-radius: 50%;
    background: var(--ink-light);
  }
  .brand-name {
    font-family: "Montserrat", sans-serif;
    font-weight: 500;
    font-size: 27px;
    line-height: 1;
    letter-spacing: 0.5px;
    color: var(--ink-light);
    text-transform: uppercase;
  }
  .identity {
    position: absolute;
    left: 105px;
    top: 250px;
  }
  .person-name {
    font-family: "Pinyon Script", cursive;
    font-size: 60px;
    line-height: 1.1;
    color: var(--ink-light);
    padding: 0 14px 4px 0;
    border-bottom: 1.5px solid var(--ink-soft);
  }
  .person-title {
    margin-top: 8px;
    font-family: "Montserrat", sans-serif;
    font-weight: 500;
    font-size: 16px;
    color: var(--ink-light);
  }
  .contact-list {
    position: absolute;
    left: 110px;
    top: 210px;
    list-style: none;
    font-family: "Montserrat", sans-serif;
    font-weight: 400;
    font-size: 21px;
    color: var(--ink-muted);
  }
  .contact-item {
    display: flex;
    align-items: center;
    gap: 16px;
    margin-bottom: 22px;
  }
  .contact-icon {
    width: 24px;
    height: 24px;
    flex: none;
    fill: none;
    stroke: var(--ink-muted);
    stroke-width: 2;
    stroke-linecap: round;
    stroke-linejoin: round;
  }
  .backdrop-circle {
    position: absolute;
    right: 90px;
    top: 50px;
    width: 260px;
    height: 260px;
    border-radius: 50%;
    background: rgba(255, 255, 255, 0.06);
  }
</style>
</head>
<body>
  <section class="card card-back">
    <div class="backdrop-circle"></div>
    <div class="brand">
      <span class="brand-mark"></span>
      <span class="brand-name">Penwarden &amp;<br>Partners</span>
    </div>
    <ul class="contact-list">
      <li class="contact-item">
        <svg class="contact-icon" viewBox="0 0 24 24"><path d="M5 3h4l2 5-3 2a11 11 0 0 0 6 6l2-3 5 2v4a2 2 0 0 1-2 2A17 17 0 0 1 3 5a2 2 0 0 1 2-2z"/></svg>
        <span>Direct: 602.555.0147</span>
      </li>
      <li class="contact-item">
        <svg class="contact-icon" viewBox="0 0 24 24"><rect x="6" y="3" width="12" height="6"/><rect x="3" y="9" width="18" height="8" rx="1"/><rect x="6" y="14" width="12" height="7"/></svg>
        <span>Fax: 623.555.0182</span>
      </li>
      <li class="contact-item">
        <svg class="contact-icon" viewBox="0 0 24 24"><rect x="3" y="5" width="18" height="14" rx="1"/><path d="M3 6l9 7 9-7"/></svg>
        <span>Lyle@PenwardenandPartners.example</span>
      </li>
      <li class="contact-item">
        <svg class="contact-icon" viewBox="0 0 24 24"><circle cx="12" cy="12" r="9"/><path d="M3 12h18M12 3c3 3 3 15 0 18M12 3c-3 3-3 15 0 18"/></svg>
        <span>www.PenwardenandPartners.example</span>
      </li>
      <li class="contact-item">
        <svg class="contact-icon" viewBox="0 0 24 24"><path d="M12 22s7-7 7-12a7 7 0 0 0-14 0c0 5 7 12 7 12z"/><circle cx="12" cy="10" r="2.5"/></svg>
        <span>4915 West Quillmoor Lane Glendale, AZ 85391</span>
      </li>
    </ul>
  </section>

  <main class="card card-front">
    <svg class="card-art" width="1050" height="600" viewBox="0 0 1050 600">
      <defs>
        <linearGradient id="band-fade" x1="0" y1="0" x2="1" y2="0">
          <stop offset="0" stop-color="#9a9a9a"/>
          <stop offset="0.35" stop-color="#ffffff"/>
          <stop offset="1" stop-color="#f0f0f0"/>
        </linearGradient>
        <radialGradient id="photo-tones" cx="0.5" cy="0.35" r="0.7">
          <stop offset="0" stop-color="#f4f4f4"/>
          <stop offset="0.55" stop-color="#b9bcc0"/>
          <stop offset="1" stop-color="#3a3d44"/>
        </radialGradient>
      </defs>
      <path class="accent-band" d="M0 150 L520 150 L610 205 L610 228 L520 190 L0 190 Z" fill="url(#band-fade)"/>
      <circle class="outer-ring" cx="800" cy="330" r="228" fill="none" stroke="#ffffff" stroke-width="3"/>
      <line class="connector" x1="1028" y1="330" x2="1050" y2="330" stroke="#ffffff" stroke-width="3"/>
      <circle class="ring-dot" cx="572" cy="330" r="7" fill="#1a1718" stroke="#ffffff" stroke-width="3"/>
      <circle class="ring-dot" cx="1028" cy="330" r="7" fill="#1a1718" stroke="#ffffff" stroke-width="3"/>
      <circle class="photo-frame" cx="800" cy="330" r="212" fill="#ffffff"/>
      <circle class="portrait" cx="800" cy="330" r="204" fill="url(#photo-tones)" role="img" aria-label="Portrait photograph of the broker in a dark suit and light green tie"/>
    </svg>

    <div class="brand">
      <span class="brand-mark"></span>
      <span class="brand-name">Penwarden &amp;<br>Partners</span>
    </div>

    <div class="identity">
      <p class="person-name">Lyle Penwarden</p>
      <p class="person-title">Designated Broker, CDPE, CNE, GRI</p>
    </div>
  </main>
</body>
</html>
```